NDF Job bank

National Dental Fellowship Needs a design for our orthodontist job bank.

We are in the process of redesigning our current job board. We would like to improve our current design, focusing on the landing page and possibly the search page. I have attached images of what we currently have in place right now.

The Landing page: Currently, I find the landing page too wordy, members get confused when using it, we need something that is easier for providers are seekers to use. Set up more user friendly. Maybe have a button for become provider and become seeker and then a modal pops up with process.. The final design for this page needs to be user friendly, organized and clean. If someone were coming to this page for the first time they would know how to become a provider.

The search page: I was thinking it would be best to have the search options on the left hand side opposed to how it is just in the middle now. all of the information currently shown on this page needs to be included. The search results need improvement on how they are displayed as well.

If you have any questions feel free to contact me.

Industry/Entity Type

Bank

Number of Pages Required

1 page

Colors
33a6d7
85cae6
0692cd

Requirements
Must have
• A Landing page that is well designed and that is made in the blue colors that are shown on the attached files of what our job bank currently looks like. I have also attached 3 photos that could be used for a masthead, but keep in mind these do not have to be used, you can use any photo you would like, these are just for your convenience.
Nice to have
• An improved search results page along with the Landing page

```html
<!DOCTYPE html>
<html lang="en">
<head>
<meta charset="utf-8">
<title>NDF Job Bank</title>
<link href="https://fonts.googleapis.com/css2?family=Bebas+Neue&family=Roboto:wght@300;400;700&display=swap" rel="stylesheet">
<style>
:root{
  --topbar:#1467a6;
  --topbar-dark:#0e558f;
  --header:#1f92c6;
  --card:#1a88c4;
  --card-top:#0d5c9c;
  --band:#0a5a99;
  --nav-muted:#86cdec;
  --footer-bg:#f5f7f8;
  --footer-link:#1d5f9f;
  --footer-head:#222;
  --muted:#666;
  --white:#fff;
}
*{box-sizing:border-box;margin:0;padding:0}
html,body{width:1200px;height:1170px;overflow:hidden}
body{font-family:"Roboto",Arial,sans-serif;background:var(--footer-bg);position:relative}
a{text-decoration:none;color:inherit}

.topbar{position:absolute;left:0;top:0;width:1200px;height:38px;background:var(--topbar)}
.utility-nav{position:absolute;left:113px;top:15px;display:flex;gap:0;font-size:10px;font-weight:700;color:var(--nav-muted)}
.utility-nav a{margin-right:16px}
.benefits{position:absolute;left:417px;top:5px;width:119px;height:30px;background:#2a8dcc;border:1px solid #3a9cd8;color:#fff;font-size:10px;font-weight:700;padding:10px 0 0 10px}
.benefits svg{position:absolute;right:9px;top:11px}
.account-zone{position:absolute;left:618px;top:0;width:530px;height:38px;background:var(--topbar-dark)}
.account{position:absolute;left:75px;top:12px;color:#fff;font-size:12px}
.social{position:absolute;left:160px;top:11px;display:flex;gap:9px}
.social span{width:15px;height:15px;border-radius:50%;background:#fff;display:block}
.search{position:absolute;left:268px;top:7px;width:204px;height:24px;background:#fff;border-radius:2px;font-size:11px;color:#8aa;padding:5px 0 0 8px}
.search svg{position:absolute;right:12px;top:5px}

.header{position:absolute;left:0;top:38px;width:1200px;height:117px;background:var(--header)}
.brand{position:absolute;left:113px;top:26px;display:flex;align-items:flex-start;gap:10px}
.brand-mark{width:54px;height:50px;background:#fff;border-radius:6px}
.brand-name{font-size:13px;line-height:14px;color:#0d4f8c;margin-top:4px}
.tagline{position:absolute;left:113px;top:85px;font-size:8px;color:#0d4f8c}
.main-nav{position:absolute;left:318px;top:51px;display:flex;gap:14px;font-size:13.5px;color:#fff}

.hero{position:absolute;left:0;top:155px;width:1200px;height:613px;
  background:linear-gradient(100deg,#5f86b6 0%,#8fb0d1 30%,#c9c6c0 55%,#e9e2d8 75%,#b9b7a8 100%)}
.band{position:absolute;left:0;top:768px;width:1200px;height:12px;background:var(--band)}

.cta{position:absolute;top:535px;width:444px;height:155px;border-radius:8px;overflow:hidden;background:var(--card);color:#fff;text-align:center}
.cta.provider{left:127px}
.cta.seeker{left:633px}
.cta .cap{position:absolute;left:0;top:0}
.cta .icon{position:absolute;left:50%;top:26px;transform:translateX(-50%)}
.cta h2{position:absolute;left:0;right:0;top:70px;font-family:"Bebas Neue",Impact,sans-serif;font-weight:400;font-size:37px;letter-spacing:.3px}
.cta p{position:absolute;left:0;right:0;top:117px;font-size:17px;font-weight:300}

.footer-links{position:absolute;left:157px;top:820px;width:900px;height:280px}
.col{position:absolute;top:0;font-size:12px}
.col h3{font-size:12px;font-weight:700;color:var(--footer-head);margin-bottom:12px}
.col a{display:block;color:var(--footer-link);height:30px}
.col.about{left:0}
.col.more{left:160px;top:4px}
.col.member{left:320px}
.col.tools{left:480px}
.col.sites{left:640px}
.badges{position:absolute;left:641px;top:133px}

.bottombar{position:absolute;left:0;top:1110px;width:1200px;height:60px;border-top:1px solid #ddd;background:var(--footer-bg);font-size:12px;color:var(--muted)}
.bottombar .row{position:absolute;left:137px;top:24px;display:flex;align-items:center}
.bottombar .sep{width:1px;height:18px;background:#ccc;margin:0 12px}
.bottombar .legal a{color:var(--footer-link);margin-right:9px}
</style>
</head>
<body>

<div class="topbar">
  <nav class="utility-nav"><a>Home</a><a>Store</a><a>Contact</a><a>NDF Member Directory</a><a>About</a></nav>
  <div class="benefits">Benefits For
    <svg width="10" height="7" viewBox="0 0 10 7"><path d="M1 1l4 4 4-4" stroke="#fff" stroke-width="2" fill="none"/></svg>
  </div>
  <div class="account-zone">
    <div class="account">join &nbsp;|&nbsp; sign in</div>
    <div class="social"><span></span><span></span><span></span><span></span></div>
    <div class="search">search
      <svg width="13" height="13" viewBox="0 0 13 13"><circle cx="5.5" cy="5.5" r="4" stroke="#1d8fd0" stroke-width="2" fill="none"/><path d="M8.5 8.5l3.5 3.5" stroke="#1d8fd0" stroke-width="2.2"/></svg>
    </div>
  </div>
</div>

<header class="header">
  <div class="brand">
    <div class="brand-mark"></div>
    <div class="brand-name">National<br>Dental<br>Fellowship</div>
  </div>
  <div class="tagline">Healthy Smiles. Every Day.</div>
  <nav class="main-nav"><a>Meetings &amp; Events</a><a>Education</a><a>Practice Management</a><a>News &amp; Publications</a><a>Library &amp; Research</a><a>Legal &amp; Advocacy</a><a>Communities</a></nav>
</header>

<section class="hero" role="img" aria-label="Photo of an orthodontist examining a smiling patient in a bright clinic"></section>

<a class="cta provider">
  <svg class="cap" width="444" height="40" viewBox="0 0 444 40"><path d="M0 0H444V12Q222 2 0 30Z" fill="var(--card-top)"/></svg>
  <svg class="icon" width="34" height="34" viewBox="0 0 34 34"><path d="M4 3h16l5 5v20H4z" fill="#fff"/><path d="M8 11h12M8 15h12M8 19h9M8 23h7" stroke="var(--card)" stroke-width="1.6"/><path d="M16 28l12-12 3 3-12 12h-3z" fill="#fff" stroke="var(--card)" stroke-width="1.2"/></svg>
  <h2>Become Provider</h2>
  <p>POST AN OPPORTUNITY OR SEARCH RESUMES</p>
</a>
<a class="cta seeker">
  <svg class="cap" width="444" height="40" viewBox="0 0 444 40"><path d="M0 0H444V12Q222 2 0 30Z" fill="var(--card-top)"/></svg>
  <svg class="icon" width="36" height="36" viewBox="0 0 36 36"><circle cx="14" cy="14" r="10" stroke="#fff" stroke-width="4" fill="none"/><path d="M21 21l10 10" stroke="#fff" stroke-width="6" stroke-linecap="round"/></svg>
  <h2>Become Seeker</h2>
  <p>FIND AN OPPORTUNITY OR UPLOAD RESUME</p>
</a>

<div class="band"></div>

<footer class="footer-links">
  <div class="col about"><h3>About NDF</h3><a>What We Do</a><a>Mission &amp; History</a><a>Governance</a><a>Financial Information</a><a>Strategic Plan</a></div>
  <div class="col more"><a>Awards</a><a>Advertise with Us</a><a>Calendar</a><a>Contact Us</a></div>
  <div class="col member"><h3>Membership</h3><a>Join</a><a>Orthodontists</a><a>Students/Residents</a><a>Orthodontic Staff</a><a>International</a><a>International Students</a></div>
  <div class="col tools"><h3>Tools</h3><a>My NDF</a><a>NDF Communities</a><a>Member Directory</a><a>Webmail</a><a>CE Manager</a></div>
  <div class="col sites"><h3>NDF Sites</h3><a>NDF Foundation</a><a>brightgrinday.org</a><a>NDF Insurance Company</a></div>
  <svg class="badges" width="215" height="110" viewBox="0 0 215 110">
    <rect x="0" y="3" width="110" height="40" rx="4" fill="#d9e8ee"/>
    <rect x="120" y="0" width="95" height="45" rx="4" fill="#d5e4ee"/>
    <rect x="8" y="58" width="88" height="45" rx="4" fill="#d5e4ee"/>
    <rect x="101" y="55" width="2" height="52" fill="#1d5f9f"/>
    <rect x="112" y="58" width="98" height="45" rx="4" fill="#d5e4ee"/>
  </svg>
</footer>

<div class="bottombar">
  <div class="row">
    <span>© 2013 National Dental Fellowship</span><span class="sep"></span>
    <span>220 Harbor View Rd. Millbrook, MO 63001</span><span class="sep"></span>
    <span>(800) 555-0142 or (314) 555-0190</span><span class="sep"></span>
    <span class="legal"><a>Terms of Use</a><a>Privacy Policy</a></span>
  </div>
</div>

</body>
</html>
```